Fernly Garage Doors Business Card

I need a Business Card for my garage door business:
Fernly Garage Doors.
please add:
logo
phone number: 833-2-FERNLY
(337-659)

email: service@fernlygaragedoors.com
website: www.fernlygaragedoors.com

The attached image is recommendation ONLY.

```html
<!DOCTYPE html>
<html lang="en">
<head>
<meta charset="utf-8">
<title>Fernly Garage Doors – Business Card</title>
<link rel="stylesheet" href="https://fonts.googleapis.com/css2?family=Open+Sans:wght@400;600;700&display=swap">
<style>
  :root {
    --teal: #55c3cf;
    --ink: #1f1d1e;
    --paper: #ffffff;
    --backdrop: #ecedef;
  }
  * { box-sizing: border-box; margin: 0; padding: 0; }
  html, body {
    width: 1137px; height: 1200px; overflow: hidden;
    background: var(--backdrop);
    font-family: "Open Sans", Arial, sans-serif;
  }
  .card {
    position: absolute; left: 118px;
    width: 900px; height: 514px;
    overflow: hidden;
    box-shadow: 0 6px 18px rgba(0,0,0,0.12);
  }
  /* back side */
  .card-back { top: 60px; background: var(--teal); }
  .card-back .corner-block {
    position: absolute; left: -60px; bottom: -60px;
    width: 300px; height: 260px;
    background: var(--paper); border-radius: 36px;
  }
  .card-back .wordmark {
    position: absolute; left: 330px; top: 200px;
    color: var(--paper); font-weight: 600; font-size: 48px;
    line-height: 1.15; letter-spacing: 0.5px;
  }
  /* front side */
  .card-front { top: 626px; background: var(--paper); }
  .brand {
    position: absolute; left: 56px; top: 52px;
    display: flex; align-items: center; gap: 26px;
  }
  .brand-square {
    width: 92px; height: 92px; background: var(--teal); border-radius: 6px;
  }
  .brand-name {
    color: var(--ink); font-weight: 600; font-size: 34px; line-height: 1.12;
  }
  .side-panel {
    position: absolute; right: -40px; top: 96px;
    width: 290px; height: 330px;
    background: var(--teal); border-radius: 30px;
  }
  .name-block { position: absolute; left: 0; top: 250px; }
  .name-bar {
    position: absolute; left: 0; top: 4px;
    width: 26px; height: 58px; background: var(--teal);
  }
  .person-name {
    position: absolute; left: 50px; top: 0;
    font-weight: 700; font-size: 33px; color: var(--ink); white-space: nowrap; line-height: 1;
  }
  .person-title {
    position: absolute; left: 50px; top: 36px;
    font-size: 22px; color: var(--ink); white-space: nowrap;
  }
  .contacts {
    position: absolute; left: 50px; top: 350px;
    list-style: none; display: flex; flex-direction: column; gap: 14px;
  }
  .contacts li {
    display: flex; align-items: center; gap: 16px;
    font-size: 25px; color: var(--ink); line-height: 1.2;
  }
  .contacts svg { width: 30px; height: 26px; flex: none; }
  .bottom-strip {
    position: absolute; left: 0; right: 0; bottom: 0; height: 22px; background: var(--teal);
  }
</style>
</head>
<body>
  <section class="card card-back" aria-label="Card back">
    <div class="corner-block"></div>
    <p class="wordmark">Fernly<br>Garage Doors</p>
  </section>

  <section class="card card-front" aria-label="Card front">
    <div class="brand">
      <div class="brand-square"></div>
      <p class="brand-name">Fernly<br>Garage Doors</p>
    </div>

    <div class="side-panel"></div>

    <div class="name-block">
      <div class="name-bar"></div>
      <p class="person-name">Your Name</p>
      <p class="person-title">Job Title</p>
    </div>

    <ul class="contacts">
      <li>
        <svg viewBox="0 0 30 26" aria-hidden="true"><path fill="#55c3cf" d="M3 8c0-4 6-6 12-6s12 2 12 6v2h-6V7c-2-1-10-1-12 0v3H3z M7 12h16l3 12H4z"/><circle cx="15" cy="18" r="3" fill="#fff"/></svg>
        <span>833 - 2 - FERNLY (337-659)</span>
      </li>
      <li>
        <svg viewBox="0 0 30 26" aria-hidden="true"><rect x="2" y="5" width="26" height="17" fill="#55c3cf"/><path d="M2 5l13 10L28 5" fill="none" stroke="#fff" stroke-width="2"/></svg>
        <span>service@fernlygaragedoors.com</span>
      </li>
      <li>
        <svg viewBox="0 0 30 26" aria-hidden="true"><circle cx="15" cy="13" r="11" fill="none" stroke="#55c3cf" stroke-width="3"/><ellipse cx="15" cy="13" rx="4.5" ry="11" fill="none" stroke="#55c3cf" stroke-width="2"/><path d="M4 13h22" stroke="#55c3cf" stroke-width="2"/></svg>
        <span>www.fernlygaragedoors.com</span>
      </li>
    </ul>

    <div class="bottom-strip"></div>
  </section>
</body>
</html>
```